New Business Card Design

We would like to refresh our business cards and make them look better. We are an IT company specialising in Cloud Services, IT Managed Services, software and hardware. I have attached a PSD of our current design. Also attached our logo.
Updates

I have uploaded all new logos in EPS format.

Can you please edit all designs to include a job title for Marcus Penn, eg. General Manager

Industry/Entity Type

Software

Colors
ffffff

Requirements
Must have
• Please use white background.
Should not have
• Black background

```html
<!DOCTYPE html>
<html lang="en">
<head>
<meta charset="utf-8">
<title>Clearpath Systems – Business Cards</title>
<link href="https://fonts.googleapis.com/css2?family=Questrial&family=Open+Sans:wght@400;600&display=swap" rel="stylesheet">
<style>
  :root {
    --backdrop: #e9e9ea;
    --card: #ffffff;
    --ink: #2f3133;
    --ink-soft: #55585c;
    --brand-red: #b5352a;
    --brand-grey: #7b838b;
    --outline: #9a9a9a;
  }
  * { margin: 0; padding: 0; box-sizing: border-box; }
  html, body {
    width: 1200px; height: 900px; overflow: hidden;
    background: var(--backdrop);
  }
  .canvas { position: relative; width: 1200px; height: 900px; }

  .card {
    position: absolute;
    width: 560px; height: 340px;
    left: 320px;
    background: var(--card);
    border-radius: 22px;
    overflow: hidden;
    box-shadow: 0 6px 18px rgba(0,0,0,0.12);
  }
  .card--front { top: 70px; }
  .card--back  { top: 490px; }

  /* Brand name block */
  .brand {
    position: absolute;
    display: flex; align-items: center; gap: 12px;
    font-family: "Questrial", sans-serif;
    color: var(--ink);
    letter-spacing: 0.18em;
    font-size: 20px;
    white-space: nowrap;
  }
  .brand__dot {
    width: 30px; height: 30px; border-radius: 50%;
    background: var(--brand-red);
    flex: none;
  }
  .card--front .brand { left: 44px; bottom: 56px; }
  .card--back .brand { right: 44px; top: 48px; font-size: 18px; }
  .card--back .brand__dot { width: 24px; height: 24px; }

  .tagline {
    position: absolute;
    right: 40px; top: 118px;
    font-family: "Open Sans", sans-serif;
    font-weight: 600;
    font-size: 11px;
    letter-spacing: 0.02em;
    color: var(--ink);
    text-transform: uppercase;
    white-space: nowrap;
  }

  .dots { position: absolute; }
  .card--front .dots { right: -14px; top: 62px; }
  .card--back .dots { left: -14px; bottom: 64px; }

  .person { position: absolute; left: 46px; top: 150px; }
  .person__name {
    font-family: "Questrial", sans-serif;
    font-weight: 400;
    font-size: 34px;
    color: var(--ink);
    letter-spacing: -0.01em;
    line-height: 1;
    white-space: nowrap;
  }
  .person__title {
    font-family: "Questrial", sans-serif;
    font-size: 14px;
    color: var(--ink-soft);
    margin-left: 62px;
    margin-top: 0;
    white-space: nowrap;
  }

  .contacts {
    position: absolute;
    right: 42px; top: 168px;
    list-style: none;
    font-family: "Questrial", sans-serif;
    font-size: 15px;
    color: var(--ink);
  }
  .contacts li {
    display: flex; align-items: center; gap: 12px;
    line-height: 22px;
    white-space: nowrap;
  }
  .contacts svg { width: 11px; height: 11px; flex: none; }
</style>
</head>
<body>
<main class="canvas">

  <section class="card card--front" aria-label="Card front">
    <svg class="dots" width="110" height="34" viewBox="0 0 110 34" aria-hidden="true">
      <circle cx="17" cy="17" r="14" fill="var(--brand-grey)"/>
      <circle cx="52" cy="17" r="14" fill="var(--brand-red)"/>
      <circle cx="88" cy="17" r="14" fill="none" stroke="var(--outline)" stroke-width="1"/>
    </svg>
    <p class="tagline">IT Services, Solutions and Support</p>
    <div class="brand"><span class="brand__dot"></span><span class="brand__name">clearpath systems</span></div>
  </section>

  <section class="card card--back" aria-label="Card back">
    <div class="brand"><span class="brand__dot"></span><span class="brand__name">clearpath systems</span></div>

    <div class="person">
      <h1 class="person__name">Marcus Penn</h1>
      <p class="person__title">general manager</p>
    </div>

    <ul class="contacts">
      <li>
        <svg viewBox="0 0 12 12" aria-hidden="true"><path d="M3 1l2 2-1 1.5c.6 1.4 1.6 2.4 3 3L8.5 6.5l2 2L9 10.5C5 10 2 7 1.5 3z" fill="none" stroke="var(--ink-soft)" stroke-width="1"/></svg>
        07 5550 1234
      </li>
      <li>
        <svg viewBox="0 0 12 12" aria-hidden="true"><rect x="3" y="1" width="6" height="10" rx="1" fill="none" stroke="var(--ink-soft)" stroke-width="1"/><circle cx="6" cy="9" r=".7" fill="var(--ink-soft)"/></svg>
        0400 555 019
      </li>
      <li>
        <svg viewBox="0 0 12 12" aria-hidden="true"><circle cx="6" cy="6" r="2" fill="none" stroke="var(--ink-soft)" stroke-width="1"/><path d="M8 6v1a1.5 1.5 0 0 0 3 0V6a5 5 0 1 0-2 4" fill="none" stroke="var(--ink-soft)" stroke-width="1"/></svg>
        mpenn@clearpathit.com.au
      </li>
      <li>
        <svg viewBox="0 0 12 12" aria-hidden="true"><path d="M1 6l5-4.5L11 6H9.5v5h-2.5V8H5v3H2.5V6z" fill="var(--ink-soft)"/></svg>
        www.clearpathit.com.au
      </li>
    </ul>

    <svg class="dots" width="110" height="34" viewBox="0 0 110 34" aria-hidden="true">
      <circle cx="22" cy="17" r="14" fill="none" stroke="var(--outline)" stroke-width="1"/>
      <circle cx="58" cy="17" r="14" fill="var(--brand-red)"/>
      <circle cx="93" cy="17" r="14" fill="var(--brand-grey)"/>
    </svg>
  </section>

</main>
</body>
</html>
```